redesign laundry perfume webshop

We want to have a custom redesign for our website.
the focus should be luxury design . Please note that our "proefpakket" product is the most sold product.
Hello when desiging. please only use our product fotos, you can edit them, but dont make it look like there are other bottles etc.
Thank you for understanding.
Please dont show in english version (text). Use our language (dutch) use existing text on our website.
Also show our other pages as wel like category and product page etc.
Netherland and belgium
perfume
Coded - Design and coding required
5+ page
Designer to choose colors to be used in the design.

```html
<!DOCTYPE html>
<html lang="nl">
<head>
<meta charset="utf-8">
<title>Linnengeur – Product categorie</title>
<link href="https://fonts.googleapis.com/css2?family=Cinzel:wght@400;700&family=Cormorant+Garamond:wght@400;500&family=Poppins:wght@400;500;600&display=swap" rel="stylesheet">
<style>
:root{
  --gold:#c8901f;
  --gold-light:#e0ac35;
  --ink:#1e1e1e;
  --line:#dcdcdc;
  --card:#f4f4f4;
  --dark:#1f1f1f;
  --darker:#262626;
  --white:#ffffff;
}
*{box-sizing:border-box;margin:0;padding:0}
html,body{width:788px;height:1200px;overflow:hidden;background:var(--white)}
body{position:relative;font-family:'Poppins',sans-serif;color:var(--ink)}
.abs{position:absolute}
.caps{font-family:'Cinzel',serif;font-variant:small-caps}

/* header */
.site-header{position:absolute;left:0;top:0;width:788px;height:67px;background:var(--white)}
.social{left:50px;top:12px;display:flex;gap:12px}
.social span{width:11px;height:11px;border-radius:50%;background:#9a9a9a;display:block}
.header-rule{top:35px;height:1px;background:var(--line)}
.phone{left:512px;top:9px;font-family:'Cormorant Garamond',serif;font-size:15px;color:var(--gold);display:flex;align-items:center;gap:8px}
.tools{left:650px;top:11px;display:flex;gap:17px;align-items:center}
.cart-count{font-size:8px;color:var(--ink);font-family:'Cormorant Garamond',serif;margin-left:-14px;margin-top:-10px}
.nav{top:41px;display:flex;gap:26px;font-family:'Cinzel',serif;font-size:14px;letter-spacing:.6px;color:var(--ink)}
.nav a{color:inherit;text-decoration:none}
.nav .active{color:var(--gold)}
.brand-tab{left:344px;top:0;width:101px;height:84px;background:var(--white);border-radius:0 0 10px 10px;display:flex;flex-direction:column;align-items:center;justify-content:center;gap:6px;z-index:3}
.brand-dot{width:30px;height:30px;border-radius:50%;background:var(--gold)}
.brand-name{font-family:'Cormorant Garamond',serif;font-size:11px;color:var(--gold);letter-spacing:.3px}

/* hero */
.hero{left:0;top:67px;width:788px;height:234px;background:linear-gradient(90deg,#0f5a55 0%,#1e3a3a 18%,#3b4a5a 45%,#5c4a3a 70%,#166a64 100%)}
.hero-title{left:53px;top:157px;font-family:'Cinzel',serif;font-weight:700;font-size:38px;color:var(--white);letter-spacing:1px}

/* categories */
.section-title{left:0;width:788px;top:344px;text-align:center;font-family:'Cinzel',serif;font-weight:700;font-size:23px;color:var(--gold);letter-spacing:1px}
.product-img{background:var(--card);display:flex;align-items:center;justify-content:center}
.bottle{width:106px;height:247px;border-radius:8px}
.product-name{font-family:'Cinzel',serif;font-size:12.5px;letter-spacing:.8px;display:flex;align-items:center;gap:12px;width:163px}
.product-name::after{content:"";flex:1;height:1px;background:var(--ink)}
.price{font-family:'Cormorant Garamond',serif;font-size:15px;color:var(--gold)}

/* features */
.features{left:0;top:865px;width:788px;height:73px;background:var(--dark)}
.feature{position:absolute;top:20px;display:flex;gap:14px;align-items:center;color:var(--white)}
.feature h3{font-family:'Cinzel',serif;font-weight:400;font-size:13px;letter-spacing:.8px;line-height:1.2}
.feature p{font-size:10px;margin-top:5px;line-height:1.2}

/* newsletter & footer */
.newsletter{left:0;top:938px;width:788px;height:262px;background:var(--darker)}
.news-title{left:0;width:788px;top:962px;text-align:center;font-family:'Cinzel',serif;font-weight:700;font-size:18px;color:var(--gold-light);letter-spacing:1px}
.news-text{left:0;width:788px;top:997px;text-align:center;font-size:11px;color:var(--white)}
.news-form{left:225px;top:1030px;width:337px;height:37px;border:1px solid #5a5a5a;border-radius:19px;display:flex;align-items:center;justify-content:space-between;padding:0 15px 0 19px;font-size:11px}
.news-form .placeholder{color:#bdbdbd}
.news-form .submit{color:var(--gold-light);font-weight:600;display:flex;align-items:center;gap:5px}
.footer-rule{left:49px;top:1103px;width:690px;height:1px;background:#4a4a4a}
.footer-nav{left:47px;top:1130px;display:flex;gap:21px;font-family:'Cinzel',serif;font-size:10.5px;color:#d8d8d8;letter-spacing:.5px}
.copyright{left:47px;top:1159px;font-size:8px;color:var(--white)}
.payments{left:502px;top:1145px;display:flex;gap:21px}
.payments span{width:28px;height:17px;background:#e9e9e9;border-radius:2px;display:block}
</style>
</head>
<body>

<header class="site-header">
  <div class="abs social"><span></span><span></span><span></span><span></span><span></span></div>
  <div class="abs header-rule" style="left:49px;width:295px"></div>
  <div class="abs header-rule" style="left:443px;width:297px"></div>
  <div class="abs phone">
    <svg width="10" height="11" viewBox="0 0 10 11"><path d="M3 1 1.5 1.5C1 4 3 8.5 6 10l1.5-.8-1.5-2.3-1.2.6C4 6.5 3.5 5 3.3 3.8l1.2-.5z" fill="#1e1e1e"/></svg>
    +31 20 555 0142
  </div>
  <div class="abs tools">
    <svg width="11" height="11" viewBox="0 0 11 11"><circle cx="4.5" cy="4.5" r="3.3" stroke="#555" stroke-width="1.5" fill="none"/><path d="M7 7l3 3" stroke="#555" stroke-width="1.6"/></svg>
    <svg width="11" height="11" viewBox="0 0 11 11"><circle cx="5.5" cy="3" r="2.6" fill="#555"/><path d="M.5 11c0-3.5 2-4.8 5-4.8s5 1.3 5 4.8z" fill="#555"/></svg>
    <svg width="12" height="10" viewBox="0 0 12 10"><path d="M0 3.5h12l-1.5 6h-9z" fill="#c8901f"/><path d="M3 3.5 5 .5M9 3.5 7 .5" stroke="#c8901f"/></svg>
    <span class="cart-count">(0)</span>
  </div>
  <nav class="abs nav caps" style="left:53px"><a class="active">Thuis</a><a>Over</a><a>Producten</a></nav>
  <nav class="abs nav caps" style="left:501px"><a>Speciaal</a><a>Recensies</a><a>Contact</a></nav>
</header>
<div class="abs brand-tab"><span class="brand-dot"></span><span class="brand-name">LINNENGEUR</span></div>

<section class="abs hero" role="img" aria-label="Foto van een rij wasparfumflesjes in een geschenkdoos op teal stof"></section>
<h1 class="abs hero-title caps">Product categorie</h1>

<h2 class="abs section-title caps">Product Categorieën</h2>

<div class="abs product-img" style="left:51px;top:407px;width:163px;height:278px"><div class="bottle" role="img" aria-label="Flesje Petal Shower met blauw-wit motief" style="background:linear-gradient(#fff 0 22%,#dce9f7 22%)"></div></div>
<div class="abs product-name" style="left:51px;top:695px">Petal Shower</div>
<div class="abs price" style="left:51px;top:713px">$14.95</div>

<div class="abs product-name" style="left:226px;top:480px">Bloom Mist</div>
<div class="abs price" style="left:226px;top:497px">$14.95</div>
<div class="abs product-img" style="left:226px;top:524px;width:163px;height:278px"><div class="bottle" role="img" aria-label="Flesje Bloom Mist met blauw bloemenmotief" style="background:linear-gradient(#fff 0 22%,#cfe2f5 22%)"></div></div>

<div class="abs product-img" style="left:401px;top:407px;width:163px;height:278px"><div class="bottle" role="img" aria-label="Flesje Sunrise Glow met oranje motief" style="background:linear-gradient(#fff 0 22%,#f2a21f 22%)"></div></div>
<div class="abs product-name" style="left:401px;top:695px">Sunrise Glow</div>
<div class="abs price" style="left:401px;top:713px">$14.95</div>

<div class="abs product-name" style="left:576px;top:480px">Dawn Breeze</div>
<div class="abs price" style="left:576px;top:497px">$14.95</div>
<div class="abs product-img" style="left:576px;top:524px;width:163px;height:278px"><div class="bottle" role="img" aria-label="Flesje Dawn Breeze met rood-wit motief" style="background:linear-gradient(#fff 0 22%,#d8a1a1 22%)"></div></div>

<section class="abs features">
  <div class="feature" style="left:54px">
    <svg width="28" height="22" viewBox="0 0 28 22"><path d="M0 2h17v14H0zM17 7h6l5 5v4H17z" fill="#d9a437"/><circle cx="6" cy="18" r="3" fill="#d9a437" stroke="#1f1f1f" stroke-width="1.5"/><circle cx="22" cy="18" r="3" fill="#d9a437" stroke="#1f1f1f" stroke-width="1.5"/></svg>
    <div><h3 class="caps">Geen verzendkosten</h3><p>Exercitation ullamco</p></div>
  </div>
  <div class="feature" style="left:264px">
    <svg width="26" height="22" viewBox="0 0 26 22"><path d="M9 2 1 9l8 7v-4c7 0 11 2 15 8-1-8-6-13-15-13z" fill="#d9a437"/></svg>
    <div><h3 class="caps">Gemakkelijk retourneren</h3><p>Exercitation ullamco</p></div>
  </div>
  <div class="feature" style="left:520px">
    <svg width="26" height="22" viewBox="0 0 26 22"><ellipse cx="10" cy="8" rx="10" ry="7" fill="#d9a437"/><ellipse cx="17" cy="14" rx="8" ry="5.5" fill="#b8862a"/><path d="M22 17l3 4-6-2z" fill="#b8862a"/></svg>
    <div><h3 class="caps" style="font-size:15px">24/7 Ondersteuning</h3><p>Exercitation ullamco</p></div>
  </div>
</section>

<section class="abs newsletter"></section>
<h2 class="abs news-title caps">Inschrijven nieuwsbrief</h2>
<p class="abs news-text">Sed ut perspiciatis unde omnis iste natus error sit voluptatem accusantium</p>
<div class="abs news-form">
  <span class="placeholder">Email Address</span>
  <span class="submit">Aanmelden
    <svg width="11" height="11" viewBox="0 0 11 11"><circle cx="5.5" cy="5.5" r="5.5" fill="#e0ac35"/><path d="M3 5.5h4.5M5.5 3.3l2.2 2.2-2.2 2.2" stroke="#262626" stroke-width="1.4" fill="none"/></svg>
  </span>
</div>
<div class="abs footer-rule"></div>
<nav class="abs footer-nav caps"><span>Thuis</span><span>Over</span><span>Producten</span><span>Speciaal</span><span>Recensies</span><span>Contact</span></nav>
<p class="abs copyright">Copyright © 2023 Linnengeur&nbsp; All Right Reserved</p>
<div class="abs payments"><span></span><span></span><span></span><span></span><span></span></div>

</body>
</html>
```